High end Electrical/home automation Business Card

Need a card for a high end electrical and home automation company utilising the existing logo.
Phone
Email
Website

Like black look with raised detail. Don’t necessarily need to keep colour of logo it could be made grayscale or white etc

Target Market(s)

High end clients

Contact Information for Business Card

Ridgeline Electrical

Requirements
Must have
• Logo, phone, email, website, address

High end look
Nice to have
• Black background card
Raised font
Should not have
• Lots of colour

```html
<!DOCTYPE html>
<html lang="en">
<head>
<meta charset="utf-8">
<title>Ridgeline Electrical – Business Card</title>
<link href="https://fonts.googleapis.com/css2?family=Lato:wght@400;700&display=swap" rel="stylesheet">
<style>
  :root {
    --backdrop: #2a2a2a;
    --card: #121212;
    --silver: #d4d4d4;
    --silver-soft: #a9a9a9;
    --rule: #5a5a5a;
  }
  * { box-sizing: border-box; margin: 0; padding: 0; }
  html, body { width: 1200px; height: 1017px; overflow: hidden; }
  body {
    background: var(--backdrop);
    font-family: "Lato", sans-serif;
    display: flex;
    flex-direction: column;
    align-items: center;
    justify-content: center;
    gap: 60px;
  }
  .card {
    width: 700px;
    height: 400px;
    background: var(--card);
    box-shadow: 0 12px 30px rgba(0,0,0,.45);
    position: relative;
  }
  .brand {
    display: flex;
    align-items: center;
    gap: 14px;
    color: var(--silver);
    font-weight: 700;
    white-space: nowrap;
  }
  .brand-dot {
    border: 2px solid var(--silver);
    border-radius: 50%;
    flex: none;
  }
  .card--front {
    display: flex;
    align-items: center;
    justify-content: center;
  }
  .card--front .brand { font-size: 40px; }
  .card--front .brand-dot { width: 30px; height: 30px; }

  .card--back { display: flex; align-items: center; }
  .card--back .brand {
    font-size: 28px;
    width: 360px;
    justify-content: center;
  }
  .card--back .brand-dot { width: 22px; height: 22px; }
  .divider {
    width: 1px;
    height: 250px;
    background: var(--rule);
  }
  .contact {
    padding-left: 34px;
    color: var(--silver);
    font-size: 15px;
    line-height: 1.45;
  }
  .contact-name {
    font-size: 22px;
    letter-spacing: 1px;
    text-transform: uppercase;
  }
  .contact-role { color: var(--silver-soft); margin-bottom: 18px; }
  .contact-address { margin-bottom: 14px; }
  .contact-line { display: flex; align-items: center; gap: 9px; }
  .contact-line svg { width: 12px; height: 12px; fill: var(--silver); flex: none; }
</style>
</head>
<body>
  <section class="card card--front">
    <div class="brand"><span class="brand-dot"></span>Ridgeline Electrical</div>
  </section>

  <section class="card card--back">
    <div class="brand"><span class="brand-dot"></span>Ridgeline Electrical</div>
    <div class="divider"></div>
    <div class="contact">
      <p class="contact-name">Daniel Hayes</p>
      <p class="contact-role">President</p>
      <p class="contact-address">Ridgeline Electrical LLC<br>1420 Birchwood Lane<br>Anchorage, Alaska 99517</p>
      <p class="contact-line">
        <svg viewBox="0 0 24 24" aria-hidden="true"><path d="M6.6 10.8a15 15 0 0 0 6.6 6.6l2.2-2.2a1 1 0 0 1 1-.25 11.4 11.4 0 0 0 3.6.6 1 1 0 0 1 1 1V20a1 1 0 0 1-1 1A17 17 0 0 1 3 4a1 1 0 0 1 1-1h3.5a1 1 0 0 1 1 1c0 1.25.2 2.45.6 3.6a1 1 0 0 1-.25 1z"/></svg>
        555-014-2873
      </p>
      <p class="contact-line">
        <svg viewBox="0 0 24 24" aria-hidden="true"><path d="M2 5h20v14H2zm2 2v.5l8 5 8-5V7zm0 2.8V17h16V9.8l-8 5z"/></svg>
        info@ridgelineelec.com
      </p>
      <p class="contact-line">
        <svg viewBox="0 0 24 24" aria-hidden="true"><path d="M12 2a10 10 0 1 0 0 20 10 10 0 0 0 0-20zm6.9 9h-3a15 15 0 0 0-1.3-5.9A8 8 0 0 1 18.9 11zM12 4.1c.9 1.2 1.8 3.6 1.9 6.9h-3.8c.1-3.3 1-5.7 1.9-6.9zM9.4 5.1A15 15 0 0 0 8.1 11h-3a8 8 0 0 1 4.3-5.9zM5.1 13h3a15 15 0 0 0 1.3 5.9A8 8 0 0 1 5.1 13zm6.9 6.9c-.9-1.2-1.8-3.6-1.9-6.9h3.8c-.1 3.3-1 5.7-1.9 6.9zm2.6-1A15 15 0 0 0 15.9 13h3a8 8 0 0 1-4.3 5.9z"/></svg>
        www.ridgelineelec.com
      </p>
    </div>
  </section>
</body>
</html>
```